Corliss Homes Website for luxury custom home builder with endless detail

Modern website for luxury custom home builder. Simple and easy for viewers to understand what we do. New company formed by retired custom home builder. Company concept is to simplify the building experience with modern technology and introduce a simple pricing strategy for the client. Website must flow. Prefer page less design or possibly something that is up and coming within the web design community. Two galleries: INTERIOR and EXTERIOR. I would like two click on box's when the website is opened showing the galleries as a centerpiece and would also prefer them to play as a slide show. The page needs to fit the entire screen in size. We would like to use Grey, Black and White or the shade of blue that is in our company logo. I would like to see one of my uploaded photos to be in the background. I would also like a 3rd box that will play some type of animated video describing what we do and what our process is. Hoping this would be more interactive for the viewer than clicking on buttons and navigating around wasting time.

Target Market(s)

affluent buyers ages 30-60 who want to built anything from large estates to downsized luzury homes for the retired crowd.

Industry/Entity Type

Home Builder

Number of Pages Required

1 page

Font styles to use
Sans Serif

Colors
33a6d7
000000
333333
5c5c5c
9d9d9d
d9d9d9

Requirements
Must have
• Logo and name at top of page. I would like a pageless web design that includes two gallery box's (Interior and Exterior photos) side by side on the first page. I would also like a 3rd box that will be a eVideo explaining what we do and how we do it. I want as little text as possible. I would like the background to be of one of my interior photos that will flow best and pop when the page loads.

```html
<!DOCTYPE html>
<html lang="en">
<head>
<meta charset="utf-8">
<title>Corliss Homes</title>
<link href="https://fonts.googleapis.com/css2?family=Cinzel:wght@700&family=Lato:wght@400;700&display=swap" rel="stylesheet">
<style>
  :root {
    --backdrop: #e2e2e2;
    --page: #f5f5f4;
    --brand-blue: #0b4ea2;
    --ink: #000000;
    --text: #333333;
    --muted: #9d9d9d;
    --rule: #d9d9d9;
    --button: #9b9b9b;
    --white: #ffffff;
  }
  * { box-sizing: border-box; margin: 0; padding: 0; }
  html, body {
    width: 1200px; height: 1200px; overflow: hidden;
    background: var(--backdrop);
    font-family: "Lato", Arial, sans-serif;
    color: var(--text);
  }
  .page {
    position: absolute; left: 61px; top: 24px;
    width: 1079px; height: 1138px;
    background: var(--page);
    box-shadow: 0 0 4px rgba(0,0,0,.08);
  }
  .abs { position: absolute; }

  /* brand */
  .brand {
    left: 40px; top: 52px; display: flex; align-items: center; gap: 8px;
  }
  .brand-square { width: 14px; height: 14px; background: var(--brand-blue); }
  .brand-name {
    font-family: "Lato", Arial, sans-serif; font-weight: 700;
    font-size: 20px; color: var(--brand-blue); letter-spacing: .3px;
  }

  /* navigation */
  .main-nav {
    left: 465px; top: 29px; display: flex; gap: 16px;
    font-size: 10.5px; color: var(--ink); letter-spacing: .2px;
  }
  .utility-nav {
    left: 884px; top: 28px; display: flex; align-items: center; gap: 10px;
    font-size: 9px; letter-spacing: 1.6px; color: var(--ink);
  }
  .utility-nav .chev { width: 8px; height: 6px; margin-left: 3px; }
  .utility-nav .item { display: flex; align-items: center; margin-right: 18px; }
  .search { left: 1025px; top: 27px; width: 11px; height: 11px; }

  /* galleries */
  .accent { background: var(--brand-blue); }
  .photo { box-shadow: 0 12px 14px -8px rgba(0,0,0,.35); }
  .photo-interior { background: linear-gradient(160deg, #d8d3cc 0%, #c5b9aa 45%, #7a5a3e 80%, #5b3d26 100%); }
  .photo-exterior { background: linear-gradient(180deg, #8d95c9 0%, #a7a8c8 35%, #c9c0b5 60%, #6d5f57 85%, #3a3430 100%); }
  .photo-estate { background: linear-gradient(180deg, #9fb8cc 0%, #b8c6cf 30%, #b7aea7 55%, #8e8984 75%, #5d7a3c 88%, #5c8a32 100%); }

  .slide-controls { display: flex; gap: 2px; }
  .slide-controls span {
    width: 22px; height: 20px; background: var(--white);
    display: flex; align-items: center; justify-content: center;
  }

  .section-title {
    font-family: "Cinzel", Georgia, serif; font-weight: 700; color: var(--ink);
    line-height: 1; letter-spacing: .5px;
  }
  .copy p { font-size: 10.9px; line-height: 13.6px; color: var(--text); margin-bottom: 13px; }

  .tags { left: 181px; top: 587px; font-size: 11.5px; line-height: 17px; color: var(--ink); letter-spacing: .3px; }
  .tag-rule { left: 59px; top: 599px; width: 111px; height: 2px; background: var(--rule); }

  .play-button { left: 303px; top: 866px; }
  .watch-button {
    left: 766px; top: 918px; width: 140px; height: 35px;
    background: var(--button); color: var(--white);
    font-size: 16px; display: flex; align-items: center; justify-content: center;
  }
  .footer {
    left: 0; top: 1111px; width: 1079px; text-align: center;
    font-size: 11px; color: var(--text);
  }
</style>
</head>
<body>
<div class="page">
  <header>
    <div class="abs brand">
      <span class="brand-square"></span>
      <span class="brand-name">Corliss Homes</span>
    </div>

    <nav class="abs main-nav">
      <span>ABOUT</span><span>WORK</span><span>LATEST</span><span>EXPLORE</span><span>AWARDS</span><span>CONTACT</span>
    </nav>
    <div class="abs utility-nav">
      <span class="item">FOLLOW
        <svg class="chev" viewBox="0 0 8 6"><path d="M1 1l3 3 3-3" fill="none" stroke="#9d9d9d" stroke-width="1"/></svg></span>
      <span class="item">INFO
        <svg class="chev" viewBox="0 0 8 6"><path d="M1 1l3 3 3-3" fill="none" stroke="#9d9d9d" stroke-width="1"/></svg></span>
    </div>
    <svg class="abs search" viewBox="0 0 11 11"><circle cx="4.5" cy="4.5" r="3.5" fill="none" stroke="#000" stroke-width="1.2"/><path d="M7 7l3.5 3.5" stroke="#000" stroke-width="1.2"/></svg>
  </header>

  <!-- interior gallery -->
  <section>
    <div class="abs accent" style="left:40px;top:133px;width:467px;height:371px"></div>
    <div class="abs photo photo-interior" role="img" aria-label="Bright white kitchen with island, pendant lights and dark wood floor" style="left:58px;top:151px;width:468px;height:368px"></div>
    <div class="abs slide-controls" style="left:471px;top:490px">
      <span><svg width="8" height="10" viewBox="0 0 8 10"><path d="M6 1L2 5l4 4" fill="none" stroke="#000" stroke-width="1.6"/></svg></span>
      <span><svg width="8" height="10" viewBox="0 0 8 10"><path d="M2 1l4 4-4 4" fill="none" stroke="#000" stroke-width="1.6"/></svg></span>
    </div>
    <h2 class="abs section-title" style="left:58px;top:544px;font-size:34px">INTERIOR DESIGN</h2>
    <div class="abs tag-rule"></div>
    <div class="abs tags">ART DIRECTION<br>INTERIOR DESIGN</div>
  </section>

  <!-- exterior gallery -->
  <section>
    <h2 class="abs section-title" style="left:569px;top:130px;font-size:36px">EXTERIOR DESIGN</h2>
    <div class="abs copy" style="left:570px;top:177px;width:466px">
      <p>Neque porro quisquam est qui dolorem ipsum quia dolor sit amet, consectetur, adipisci velit.There is no one who loves pain itself, who seeks after it and wants to have it, simply because it is pain.</p>
      <p>Lorem Ipsum is simply dummy text of the printing and typesetting industry. Lorem Ipsum has been the industry's standard dummy text ever since the 1500s, when an unknown printer took a galley of type and scrambled it to make a type specimen book.</p>
    </div>
    <div class="abs photo-exterior" role="img" aria-label="Modern two-storey stucco house at dusk with lit wooden front door and paved path" style="left:570px;top:291px;width:452px;height:367px"></div>
    <div class="abs slide-controls" style="left:965px;top:630px">
      <span><svg width="8" height="10" viewBox="0 0 8 10"><path d="M6 1L2 5l4 4" fill="none" stroke="#000" stroke-width="1.6"/></svg></span>
      <span><svg width="8" height="10" viewBox="0 0 8 10"><path d="M2 1l4 4-4 4" fill="none" stroke="#000" stroke-width="1.6"/></svg></span>
    </div>
  </section>

  <!-- video -->
  <section>
    <div class="abs accent" style="left:67px;top:706px;width:675px;height:371px"></div>
    <div class="abs photo photo-estate" role="img" aria-label="Large stone estate with turrets and arched windows at twilight, lawn in front" style="left:40px;top:723px;width:684px;height:367px"></div>
    <svg class="abs play-button" width="80" height="80" viewBox="0 0 80 80" aria-label="Play video">
      <circle cx="40" cy="40" r="36" fill="none" stroke="#fff" stroke-width="4.5"/>
      <path d="M31 24l25 16-25 16z" fill="#fff"/>
    </svg>
    <h2 class="abs section-title" style="left:763px;top:720px;font-size:30px">OUR VIDEO</h2>
    <div class="abs copy" style="left:766px;top:765px;width:262px">
      <p>Neque porro quisquam est qui dolorem ipsum quia dolor sit amet, consectetur, adipisci velit.There is no one who loves pain itself, who seeks after it and wants to have it, simply because it is pain.</p>
      <p>Lorem Ipsum is simply dummy text of the printing and typesetting industry. Lorem Ipsum has been the industry's standard dummy text ever since the 1500s, when an unknown printer took a galley of type and scrambled it to make a type specimen book.</p>
    </div>
    <div class="abs watch-button">Watch more video</div>
  </section>

  <footer class="abs footer">Corliss homes @ Copyright 2015, All rights reserved &nbsp;|&nbsp; Privacy policy</footer>
</div>
</body>
</html>
```